Corportate Power Point Template

We need a corporate PPT Design for our startup Big Data company.

Basically, our company will ingest, analyze and generate dynamic Dashboards with data consumed from different sources like Social Networks, Enterprise Legacy Systems such as e-Commerce, ERP, CRM and others.

Company is headquartered in Brazil, but will have a global presence.

Industry/Entity Type

It Company

```html
<!DOCTYPE html>
<html lang="en">
<head>
<meta charset="UTF-8">
<title>Title Presentation</title>
<link href="https://fonts.googleapis.com/css2?family=PT+Sans:wght@400;700&display=swap" rel="stylesheet">
<style>
  :root {
    --orange: #e8801f;
    --band: #e36c0a;
    --title: #58585a;
    --body: #58585a;
    --paper: #ffffff;
  }
  html, body {
    margin: 0;
    padding: 0;
    overflow: hidden;
    background: var(--paper);
  }
  .slide {
    position: relative;
    width: 1200px;
    height: 675px;
    overflow: hidden;
    background: var(--paper);
    font-family: "PT Sans", Arial, sans-serif;
  }
  .corner-mark {
    position: absolute;
    left: 6px;
    top: 4px;
    width: 90px;
    height: 90px;
    background: linear-gradient(135deg, #e8561a 0%, #f29a3a 60%, rgba(248, 190, 120, 0.3) 100%);
    clip-path: polygon(0 0, 100% 0, 100% 35%, 45% 100%, 0 100%);
  }
  .title {
    position: absolute;
    left: 132px;
    top: 18px;
    margin: 0;
    font-size: 46px;
    font-weight: 700;
    letter-spacing: 0.2px;
    color: var(--title);
    line-height: 1;
  }
  .title-rule {
    position: absolute;
    left: 134px;
    top: 72px;
    width: 987px;
    height: 1px;
    background: var(--orange);
  }
  .subtitle {
    position: absolute;
    left: 134px;
    top: 79px;
    margin: 0;
    font-size: 28px;
    font-weight: 700;
    color: var(--orange);
    line-height: 1.2;
  }
  .column {
    position: absolute;
    top: 180px;
    width: 466px;
    color: var(--body);
    font-size: 20.5px;
    line-height: 28px;
    text-align: justify;
  }
  .column p { margin: 0 0 28px; }
  .column-left { left: 90px; }
  .column-right { left: 619px; width: 502px; }
  .footer-band {
    position: absolute;
    left: 0;
    bottom: 0;
    width: 1200px;
    height: 38px;
  }
  .brand {
    position: absolute;
    left: 856px;
    top: 620px;
    width: 242px;
    text-align: center;
    font-size: 30px;
    font-weight: 700;
    color: var(--orange);
    line-height: 1;
  }
</style>
</head>
<body>
  <main class="slide">
    <div class="corner-mark" role="img" aria-label="Decorative cluster of orange squares"></div>

    <h1 class="title">TITLE PRESENTATION</h1>
    <div class="title-rule"></div>
    <h2 class="subtitle">Sub Title Presentation</h2>

    <section class="column column-left">
      <p>Lorem ipsum dolor sit amet, consectetuer adipiscing elit. Maecenas porttitor congue massa. Fusce posuere, magna sed pulvinar ultricies, purus lectus malesuada libero, sit amet commodo magna eros quis urna.</p>
      <p>Lorem ipsum dolor sit amet, consectetuer adipiscing elit. Maecenas porttitor congue massa. Fusce posuere, magna sed pulvinar ultricies, purus lectus malesuada libero, sit amet commodo magna eros quis urna.</p>
      <p>Nunc viverra imperdiet enim. Fusce est. Vivamus a tellus.</p>
    </section>

    <section class="column column-right">
      <p>Lorem ipsum dolor sit amet, consectetuer adipiscing elit. Maecenas porttitor congue massa. Fusce posuere, magna sed pulvinar ultricies, purus lectus malesuada libero, sit amet commodo magna eros quis urna.</p>
      <p>Lorem ipsum dolor sit amet, consectetuer adipiscing elit. Maecenas porttitor congue massa. Fusce posuere, magna sed pulvinar ultricies, purus lectus malesuada libero, sit amet commodo magna eros quis urna.</p>
      <p>Nunc viverra imperdiet enim. Fusce est. Vivamus a tellus.</p>
    </section>

    <svg class="footer-band" viewBox="0 0 1200 38" aria-hidden="true">
      <rect x="0" y="0" width="1200" height="38" fill="var(--band)"/>
      <polygon points="827,0 856,38 1097,38 1125,0" fill="var(--paper)"/>
    </svg>

    <div class="brand">Vantora Labs</div>
  </main>
</body>
</html>
```